Business cards and stationery for new company logo
TRV Enterprises
Business cards and stationery for new company logo - Construction
Creative Brief
Simple
Marcus Pellham
Owner
742 Wildrow Ave. Brennmoor, Westvale K4T 2B5
marcus@trventerprises.ca
www.trventerprises.ca
Would like something sleek and corporate looking. Catchy. The logo that was designed has all those elements...I would like the bus cards and stationery to also have those.

```html
<!DOCTYPE html>
<html lang="en">
<head>
<meta charset="utf-8">
<title>TRV Enterprises – Business Cards</title>
<link href="https://fonts.googleapis.com/css2?family=Michroma&display=swap" rel="stylesheet">
<style>
  :root {
    --bg: #e9e9eb;
    --card-white: #ffffff;
    --card-black: #1e1b1b;
    --ink: #2a2a2a;
    --muted: #6b6b6b;
    --red: #e0221f;
    --red-dark: #b5141a;
    --light: #e6e6e6;
  }
  * { margin: 0; padding: 0; box-sizing: border-box; }
  html, body { width: 1200px; height: 1006px; overflow: hidden; }
  body {
    background: var(--bg);
    font-family: "Michroma", "Arial", sans-serif;
    position: relative;
  }
  .card {
    position: absolute;
    border-radius: 22px;
    overflow: hidden;
    box-shadow: 0 6px 18px rgba(0,0,0,0.18);
  }
  /* Back of card */
  .card-back {
    left: 560px; top: 150px;
    width: 580px; height: 331px;
    background: var(--card-black);
  }
  .card-back .brand {
    position: absolute;
    left: 0; right: 0; top: 118px;
    text-align: center;
    color: var(--light);
    font-size: 40px;
    letter-spacing: 2px;
  }
  .card-back .web {
    position: absolute;
    left: 0; right: 0; top: 214px;
    text-align: center;
    color: #bdbdbd;
    font-size: 11px;
    letter-spacing: 6px;
    text-transform: uppercase;
  }
  /* Front of card */
  .card-front {
    left: 60px; top: 500px;
    width: 620px; height: 354px;
    background: var(--card-white);
  }
  .card-front .brand {
    position: absolute;
    left: 40px; top: 34px;
    color: var(--red);
    font-size: 30px;
    letter-spacing: 1px;
  }
  .contact {
    position: absolute;
    left: 40px; top: 100px;
    list-style: none;
  }
  .contact li {
    display: flex;
    align-items: center;
    gap: 10px;
    color: var(--muted);
    font-size: 10px;
    letter-spacing: 1px;
    line-height: 21px;
  }
  .contact .dot {
    width: 9px; height: 9px;
    border-radius: 50%;
    background: var(--red);
    flex: none;
  }
  .contact .indent { padding-left: 19px; }
  .swoosh {
    position: absolute;
    left: 0; bottom: 0;
    width: 620px; height: 120px;
  }
  .card-front .web {
    position: absolute;
    left: 250px; bottom: 17px;
    color: #cfcfcf;
    font-size: 10px;
    letter-spacing: 4px;
    text-transform: uppercase;
  }
  .person {
    position: absolute;
    right: 44px; top: 200px;
    text-align: right;
  }
  .person .name {
    color: var(--red);
    font-size: 12px;
    letter-spacing: 2px;
  }
  .person .role {
    color: var(--muted);
    font-size: 9px;
    letter-spacing: 2px;
    margin-top: 5px;
  }
</style>
</head>
<body>

<section class="card card-back">
  <div class="brand">TRV Enterprises</div>
  <div class="web">www.trventerprises.ca</div>
</section>

<section class="card card-front">
  <div class="brand">TRV Enterprises</div>

  <ul class="contact">
    <li><span class="dot"></span>742 Wildrow Ave.</li>
    <li class="indent">Brennmoor, Westvale</li>
    <li class="indent">K4T 2B5</li>
    <li><span class="dot"></span>T: 613-555-0142</li>
    <li><span class="dot"></span>F: 613-555-0143</li>
    <li><span class="dot"></span>marcus@trventerprises.ca</li>
    <li><span class="dot"></span>www.trventerprises.ca</li>
  </ul>

  <div class="person">
    <div class="name">Marcus Pellham</div>
    <div class="role">Owner</div>
  </div>

  <svg class="swoosh" viewBox="0 0 620 120" aria-hidden="true">
    <path d="M0 22 Q120 82 250 66 L620 66 L620 120 L0 120 Z" fill="var(--red)"/>
    <path d="M0 50 Q120 104 250 78 L620 78 L620 120 L0 120 Z" fill="var(--red-dark)"/>
    <path d="M170 120 Q200 72 262 72 L620 72 L620 120 Z" fill="var(--card-black)"/>
  </svg>
  <div class="web">www.trventerprises.ca</div>
</section>

</body>
</html>
```